Birch Haven Sales Aid and Contract

I started my own company and the company I worked for has a sales aid / contract that I want to replicate. I want it to be simpler similar design in an editable PDF Form. It needs to be different and better in my company colors see logo attached I need to be able to edit the fine print and will need the Birch Haven changed to Birch Haven through out the agreement. Follow same flow but instead of Platinum Gold and Silver I would like Gold Silver and Bronze with different badges

```html
<!DOCTYPE html>
<html lang="en">
<head>
<meta charset="utf-8">
<title>Birch Haven Sales Aid and Contract</title>
<link href="https://fonts.googleapis.com/css2?family=Lato:ital,wght@0,400;0,700;1,400&family=Bebas+Neue&family=Oswald:wght@600&family=Poppins:wght@400;600;700&family=Open+Sans:wght@700;800&family=Great+Vibes&family=Russo+One&display=swap" rel="stylesheet">
<style>
:root{
  --teal:#0a3b3c;
  --teal-dark:#072d2e;
  --stage:#bfbfbf;
  --paper:#ffffff;
  --mist:#f3f4fb;
  --rule:#9aa3a8;
  --ink:#1f2a2b;
  --grey:#a4a7a9;
  --navy:#2c4a9a;
}
*{margin:0;padding:0;box-sizing:border-box}
html,body{width:683px;height:1200px;overflow:hidden;background:var(--stage)}
body{position:relative;font-family:"Lato",sans-serif;color:var(--ink)}
.page{position:absolute;left:135px;width:413px;height:321px;box-shadow:3px 4px 6px rgba(0,0,0,.35);overflow:hidden}
.cover{top:103px;background:var(--teal)}
.intake{top:448px;background:var(--paper)}
.guarantee{top:795px;background:var(--paper)}
.abs{position:absolute}

/* cover */
.brand{left:118px;top:14px;display:flex;align-items:center;gap:8px}
.brand-dot{width:42px;height:42px;border-radius:50%;background:var(--grey)}
.brand-name{font-family:"Russo One",sans-serif;color:var(--grey);font-size:13px;letter-spacing:2px;line-height:1}
.pill{top:67px;height:19px;background:var(--teal-dark);border-radius:4px;color:#d6dadb;font-size:8.6px;display:flex;align-items:center;padding-left:7px;font-family:"Poppins",sans-serif;font-weight:400}
.pill.license{left:16px;width:174px}
.pill.client{left:198px;width:203px}
.client .dots{flex:1;border-bottom:1px dotted #c9cfd0;margin:0 9px 0 3px;height:7px}
.photo{border:3px solid #fff;background:linear-gradient(135deg,#cfd6de,#8a97a6 55%,#5b6770)}
.photo.discovery{left:15px;top:98px;width:203px;height:133px;border-radius:4px 18px 4px 18px}
.photo.design{left:227px;top:118px;width:171px;height:92px;border-radius:4px 14px 4px 14px;background:linear-gradient(100deg,#f1ece6 0%,#e5e8ee 45%,#3f78d6 100%)}
.label{font-family:"Poppins",sans-serif;font-weight:700;color:#fff;font-size:11.5px;letter-spacing:.3px;transform:translateX(-50%)}
.headline{left:80px;top:268px;font-family:"Bebas Neue",sans-serif;color:var(--teal);font-size:26px;line-height:22px;letter-spacing:0;white-space:nowrap;transform:scaleX(.9);transform-origin:left top}

/* intake */
.top-rule{left:0;top:23px;width:413px;height:11px;border-top:1px solid var(--rule);border-bottom:1px solid var(--rule)}
.head-row{top:24px;height:10px;font-size:5.6px;display:flex;align-items:center}
.head-row b{color:var(--teal)}
.tabbed{left:97px;top:24px;width:175px;height:10px;background:#eceef0;border-radius:5px;font-weight:700;font-size:5.6px;display:flex;align-items:center;justify-content:center}
.field{left:15px;width:137px;font-size:5.6px;display:flex;align-items:flex-end}
.fill{flex:1;border-bottom:.6px dotted #6f7678;margin-left:2px;height:4px}
.project{left:160px;top:41px;width:243px;height:83px;background:var(--mist);border-radius:5px;border-top:1px solid var(--teal)}
.project-tab{left:66px;top:-1px;width:108px;height:10px;background:var(--teal);color:#fff;font-size:5.6px;display:flex;align-items:center;justify-content:center;clip-path:polygon(0 0,100% 0,92% 100%,8% 100%)}
.q{left:15px;width:378px;font-size:5.6px;display:flex;align-items:flex-end}
.q b{margin-right:2px}
.timeline{left:178px;top:248px;width:56px;height:9px;background:#eceef6;border-radius:5px;color:var(--navy);font-size:5.6px;display:flex;align-items:center;justify-content:center}
.foot-band{left:0;bottom:0;width:413px;height:10px;background:var(--teal)}

/* guarantee */
.g-title{left:0;width:413px;top:13px;text-align:center;font-family:"Open Sans",sans-serif;font-weight:800;font-size:19.5px;color:var(--teal);letter-spacing:.1px}
.g-body{left:46px;width:321px;text-align:center;font-size:5.6px;line-height:7.4px}
.g-body h3{font-family:"Open Sans",sans-serif;font-weight:800;color:var(--teal);font-size:9px;line-height:10px}
.signature{left:0;width:413px;top:237px;text-align:center;font-family:"Great Vibes",cursive;font-size:13px;color:var(--ink)}
.g-brand{left:0;width:413px;top:272px;text-align:center}
.g-brand .brand-name{font-size:7.5px;letter-spacing:1.5px}
</style>
</head>
<body>

<section class="page cover">
  <div class="abs brand">
    <span class="brand-dot"></span>
    <div class="brand-name">BIRCH HAVEN</div>
  </div>
  <div class="abs pill license">LIC. #: BC481207 &nbsp;|&nbsp; Licensed &amp; Insured</div>
  <div class="abs pill client">Client <span class="dots"></span></div>

  <div class="abs photo discovery" role="img" aria-label="Photo of a consultant meeting with an older couple at a table"></div>
  <div class="abs label" style="left:116px;top:236px">DISCOVERY</div>
  <div class="abs label" style="left:313px;top:95px">DESIGN</div>
  <div class="abs photo design" role="img" aria-label="Illustration of a hand sketching a modern house"></div>

  <svg class="abs" style="left:0;top:0" width="413" height="321" viewBox="0 0 413 321">
    <defs>
      <linearGradient id="gold" x1="0" y1="0" x2="0" y2="1"><stop offset="0" stop-color="#f3c14c"/><stop offset="1" stop-color="#8a1c14"/></linearGradient>
      <linearGradient id="silver" x1="0" y1="0" x2="0" y2="1"><stop offset="0" stop-color="#dfe3ea"/><stop offset=".5" stop-color="#6f7785"/><stop offset="1" stop-color="#4b525d"/></linearGradient>
      <linearGradient id="bronze" x1="0" y1="0" x2="0" y2="1"><stop offset="0" stop-color="#f8b45a"/><stop offset="1" stop-color="#c8721e"/></linearGradient>
    </defs>
    <path d="M0 262 H40 a30 30 0 0 1 0 59 H0Z" fill="#9ea2a6"/>
    <path d="M62 262 H200 Q208 262 214 268 L250 308 Q256 316 264 316 H413 V321 H62 Q68 292 62 262Z" fill="#fff"/>
    <circle cx="28" cy="292" r="21" fill="#d3a53a" stroke="#1b1b1b" stroke-width="3"/>
    <g font-family="Oswald,sans-serif" font-size="7.5" fill="#fff" text-anchor="middle">
      <path d="M241 232 Q263 238 285 232 V262 Q276 274 263 280 Q250 274 241 262Z" fill="url(#gold)" stroke="#f2c550" stroke-width="2"/>
      <text x="263" y="255">GOLD</text>
      <path d="M298 232 Q320 238 342 232 V262 Q333 274 320 280 Q307 274 298 262Z" fill="url(#silver)" stroke="#e8ebef" stroke-width="2"/>
      <text x="320" y="255">SILVER</text>
      <path d="M354 232 Q376 238 398 232 V262 Q389 274 376 280 Q363 274 354 262Z" fill="url(#bronze)" stroke="#f7c27a" stroke-width="2"/>
      <text x="376" y="255">BRONZE</text>
    </g>
  </svg>
  <div class="abs headline">HELPING PEOPLE<br>LASTING RESULTS</div>
  <div class="abs label" style="left:320px;top:291px">OPTIONS</div>
</section>

<section class="page intake">
  <div class="abs top-rule"></div>
  <div class="abs head-row" style="left:15px"><b>Incoming call :</b>&nbsp;Date: 3/7/24</div>
  <div class="abs tabbed">Owner of property: (YES) (NO) Date of appointment: 4/10/24</div>
  <div class="abs head-row" style="left:280px">Exterior - Interior - Masonry - Concrete - Home</div>

  <div class="abs field" style="top:43px">Name:<span class="fill"></span></div>
  <div class="abs field" style="top:53px">Address:<span class="fill"></span></div>
  <div class="abs field" style="top:63px">Best contact number:<span class="fill"></span></div>
  <div class="abs field" style="top:74px">Best e-mail:<span class="fill"></span></div>
  <div class="abs field" style="top:84px">City:<span class="fill"></span></div>
  <div class="abs field" style="top:94px">Other Decision Makers:<span class="fill"></span></div>
  <div class="abs field" style="top:104px">Contact Number<span class="fill"></span></div>
  <div class="abs field" style="top:116px;font-style:italic">After initial introduction on location</div>

  <div class="abs project"><div class="abs project-tab">Tell me a little about your project:</div></div>

  <div class="abs q" style="top:132px"><b>1.</b>Would it be ok if we discuss some of the details regarding your project? …. this will help insure we get the results your looking for!</div>
  <div class="abs q" style="top:149px"><b>2.</b>Do you have any sketches or drawings? If yes, would you mind sharing them with me? If no, that’s ok we will cover that today!</div>
  <div class="abs q" style="top:166px"><b>3.</b>Is there anything else you don’t like about your existing<span class="fill"></span></div>
  <div class="abs q" style="top:183px"><b>4.</b>Have you ever done a construction project? Y / N<span class="fill"></span></div>
  <div class="abs q" style="top:200px"><b>5.</b>What’s the biggest thing your hoping to achieve by doing<span class="fill" style="flex:0 0 42px"></span>&nbsp;?<span class="fill"></span></div>
  <div class="abs q" style="top:217px"><b>6.</b>Do you have any questions or concerns about any other portion of your property or home<span class="fill"></span>?</div>
  <div class="abs q" style="top:234px"><b>7.</b>Hypothetically if you were to move forward, how do you envision this project to go as far as time lines and completions dates?</div>
  <div class="abs q" style="top:252px">Start date<span class="fill"></span><span style="width:62px"></span><span class="fill"></span>Finish date</div>
  <div class="abs timeline">TIME LINE DATE</div>
  <div class="abs q" style="top:270px"><b>8.</b>Service Type:<span class="fill"></span>Project Manager:<span class="fill"></span>Crew:<span class="fill"></span></div>
  <div class="abs q" style="top:287px"><b>9.</b>Safety Concerns:<span class="fill"></span></div>
  <div class="abs foot-band"></div>
</section>

<section class="page guarantee">
  <h1 class="abs g-title">10 YEAR WORKMANSHIP GUARANTEE</h1>
  <svg class="abs" style="left:0;top:0" width="413" height="321" viewBox="0 0 413 321">
    <g fill="none" stroke="var(--navy)" stroke-width=".8">
      <path d="M172 75 H45 Q40 75 40 80 M30 90 V292 M383 90 V292 M241 75 H368 Q373 75 373 80 M45 305 H368"/>
      <path d="M40 80 Q38 88 30 90 M373 80 Q375 88 383 90 M30 292 Q38 294 40 300 Q40 305 45 305 M383 292 Q375 294 373 300 Q373 305 368 305"/>
      <circle cx="40" cy="80" r="3"/><circle cx="373" cy="80" r="3"/><circle cx="40" cy="300" r="3"/><circle cx="373" cy="300" r="3"/>
    </g>
    <circle cx="206" cy="74" r="29" fill="#d3a53a" stroke="#1b1b1b" stroke-width="4"/>
  </svg>
  <div class="abs g-body" style="top:115px">Your Platinum investment is stamped with a 10 year workmanship guarantee! Birch Haven’s platinum investment warrants our project to be free from defects in workmanship from date of installation to the original owner with an 10 year workmanship guarantee.
    <h3>TERMS:</h3>
    Your 10 year guarantee is on workmanship and not a materials warranty, materials would be covered under the manufacturers warranty. This 10 year guarantee is non-transferable from original owner and is void upon resale of unconditional guarantee workmanship.
    <h3>QUALIFICATION:</h3>
    Your investment of the Platinum System must be paid in full. During the terms of your 10 year workmanship guarantee, if defects in workmanship are found, original home owner must notify Birch Haven within 10 days by telephone or e-mail and confirm by written notice.
    <div style="margin-top:3px"><b>Limitations:</b> Guarantee does not cover acts of omissions of other trades, natural weathering, recommended maintenance, lightning, flood, earthquake or any natural disaster or unusual phenomenon of elements.</div>
  </div>
  <div class="abs signature">Dale Morrow - Founder</div>
  <div class="abs g-brand"><div class="brand-name">BIRCH HAVEN</div></div>
  <div class="abs foot-band"></div>
</section>

</body>
</html>
```